Corporate Dinner Invite at Verolla for PMV

PMV is hosting a corporate dinner at the BRQ Conference and we need an email attachment invite for the event. Please use some images from this site for inspiration: https://www.verollaexample.com/fernparlor/

Invite Title:
Join us for dinner!

Event Details:
Tuesday, October 24th 2023 at 6:30pm
Verolla Chicago, Fern Parlor
347 W Harlow Ave, Chicago, IL 60622

Target Market(s)

Corporate Audience

Font styles to use
Script

Colors
0054AA
0677BA
7BADD7
CADEEF
E8F1F8

Requirements
Must have
• PMV logo, event date / time, event location details, photo(s) from Fern Parlor

```html
<!DOCTYPE html>
<html lang="en">
<head>
<meta charset="utf-8">
<title>PMV Dinner Invite</title>
<link rel="stylesheet" href="https://fonts.googleapis.com/css2?family=Kaushan+Script&family=Yellowtail&family=Montserrat:wght@400;700&family=Crimson+Text:ital@1&display=block">
<style>
  :root {
    --frame: #00aeef;
    --paper: #ffffff;
    --ink: #3f3f93;
    --accent: #00aeef;
    --gold: #e2b55a;
    --brand: #1f3d7a;
    --script: "Kaushan Script", "Yellowtail", "Brush Script MT", cursive;
  }
  * { margin: 0; padding: 0; box-sizing: border-box; }
  html, body { width: 798px; height: 1200px; overflow: hidden; background: var(--frame); }
  .invite {
    position: relative; width: 798px; height: 1200px;
    background: var(--paper); border: 18px solid var(--frame); overflow: hidden;
  }
  .brand {
    position: absolute; top: 130px; left: 0; width: 762px;
    display: flex; justify-content: center; align-items: center; gap: 12px;
    font-family: "Montserrat", sans-serif; font-weight: 700; font-size: 44px; line-height: 1; color: var(--brand);
  }
  .brand-mark { width: 30px; height: 30px; background: var(--brand); }
  .title-main {
    position: absolute; top: 255px; left: 70px; width: 640px; text-align: center;
    font-family: var(--script); font-weight: 400; font-size: 190px; line-height: 1;
    color: var(--ink); text-shadow: 3px 4px 0 var(--accent);
    transform: rotate(-5deg); z-index: 1;
  }
  .title-lead {
    position: absolute; top: 262px; left: 418px; z-index: 2;
    font-family: var(--script); font-size: 52px; line-height: 1; color: var(--gold);
    transform: rotate(-4deg); white-space: nowrap;
  }
  .gallery { position: absolute; top: 510px; left: 60px; width: 640px; height: 240px; }
  .photo {
    position: absolute; border: 4px solid #fff;
    box-shadow: 0 4px 10px rgba(0,0,0,.25);
  }
  .photo-drinks { left: 22px; top: 40px; width: 230px; height: 150px; transform: rotate(17deg);
    background: linear-gradient(135deg, #3a2414, #b27a34 55%, #e8d9c2); }
  .photo-dining { left: 205px; top: 40px; width: 230px; height: 150px; transform: rotate(15deg);
    background: linear-gradient(135deg, #3b2a1e, #8a6440 60%, #cfb591); }
  .photo-bar { left: 395px; top: 50px; width: 250px; height: 160px; transform: rotate(16deg);
    background: linear-gradient(135deg, #2c1d14, #9b6a34 55%, #6e4b33); }
  .venue-line {
    position: absolute; top: 750px; left: 0; width: 762px; text-align: center;
    font-family: "Montserrat", sans-serif; font-size: 34px; line-height: 1; color: var(--accent); letter-spacing: 1px;
  }
  .details { font-family: "Crimson Text", serif; font-style: italic; color: var(--ink); }
  .details-heading {
    position: absolute; top: 800px; left: 158px; width: 454px;
    display: flex; align-items: center; gap: 16px; font-size: 36px; font-weight: 400; line-height: 1.1;
  }
  .details-heading::before, .details-heading::after {
    content: ""; flex: 1; height: 2px; background: var(--gold);
  }
  .detail { position: absolute; left: 154px; display: flex; align-items: center; gap: 18px; line-height: 1.1; }
  .detail svg { width: 28px; height: 28px; flex: none; }
  .detail-date { top: 835px; font-size: 40px; }
  .detail-time { top: 878px; font-size: 40px; }
  .detail-place { top: 924px; font-size: 29px; align-items: flex-start; line-height: 34px; }
  .detail-place svg { margin-top: 4px; }
  .sign-off {
    position: absolute; top: 1010px; left: 0; width: 762px; text-align: center;
    font-family: var(--script); font-size: 60px; line-height: 1.2; color: var(--gold);
    transform: rotate(-4deg);
  }
</style>
</head>
<body>
<main class="invite">
  <div class="brand"><span class="brand-mark"></span>PMV</div>

  <h1 class="title-main">Dinner</h1>
  <p class="title-lead">Join us for</p>

  <div class="gallery">
    <div class="photo photo-drinks" role="img" aria-label="Photo of cocktails on the bar at Fern Parlor"></div>
    <div class="photo photo-dining" role="img" aria-label="Photo of the Fern Parlor dining room with arched alcoves"></div>
    <div class="photo photo-bar" role="img" aria-label="Photo of the warmly lit bar and lounge seating"></div>
  </div>

  <p class="venue-line">@ BRQ Conference</p>

  <section class="details">
    <h2 class="details-heading">Event Details</h2>
    <p class="detail detail-date">
      <svg viewBox="0 0 28 28" aria-hidden="true"><rect x="1" y="4" width="26" height="22" fill="none" stroke="#e2b55a" stroke-width="2"/><rect x="1" y="4" width="26" height="5" fill="#e2b55a"/><rect x="6" y="1" width="2" height="5" fill="#e2b55a"/><rect x="20" y="1" width="2" height="5" fill="#e2b55a"/><g fill="#e2b55a"><rect x="5" y="12" width="3" height="3"/><rect x="10" y="12" width="3" height="3"/><rect x="15" y="12" width="3" height="3"/><rect x="20" y="12" width="3" height="3"/><rect x="5" y="18" width="3" height="3"/><rect x="10" y="18" width="3" height="3"/><rect x="15" y="18" width="3" height="3"/><rect x="20" y="18" width="3" height="3"/></g></svg>
      Tuesday, October 24th, 2023
    </p>
    <p class="detail detail-time">
      <svg viewBox="0 0 28 28" aria-hidden="true"><circle cx="14" cy="14" r="12" fill="none" stroke="#e2b55a" stroke-width="2"/><path d="M14 7v7l6 4" fill="none" stroke="#e2b55a" stroke-width="2"/></svg>
      6:30pm
    </p>
    <p class="detail detail-place">
      <svg viewBox="0 0 28 28" aria-hidden="true"><circle cx="14" cy="14" r="12" fill="none" stroke="#e2b55a" stroke-width="2"/><path d="M14 21s-5-5-5-9a5 5 0 0 1 10 0c0 4-5 9-5 9z" fill="none" stroke="#e2b55a" stroke-width="2"/><circle cx="14" cy="12" r="1.8" fill="#e2b55a"/></svg>
      <span>Verolla Chicago, Fern Parlor<br>347 W Harlow Ave, Chicago, IL 60622</span>
    </p>
  </section>

  <p class="sign-off">See You There!</p>
</main>
</body>
</html>
```